Fancy flyer to entice High School Students

http://tarnvelsw.com needs a marketing slick/flyer to pass out. The marketing text is below(feel free to place where you think appropriate).

* 8th grade to 12th grade (or 8th graders to 12th graders)
* Land a real job internship(instead of Krovetts)
* 100's of internships available
* Learn how to start your own business out of High School making way more than minimum wage
* In college when interviewing for an internship don't be the guy that answers "no, sorry, this would be my first internship" putting you at a huge disadvantage"
* Fill in the Contact Us form at http://tarnvelsw.com at the bottom left corner to find out more information

We will be evaluating design with this blog post in mind....
http://yourpostingpulse.com/color-influence-buyers/

We like attention grabbing contact us type stuff and calls to action. If you feel it is appropriate to change the marketing text to make your flyer stand out, please feel free. I am not the best at marketing and am the first to admit it.
Updates

A simple 8.5 x 11 flyer would be great.

Target Market(s)

High School students, male and female with high grade point averages(smart students). For the top 20% of their class.

Industry/Entity Type

Marketing

Requirements
Must have
• good call to action

```html
<!DOCTYPE html>
<html lang="en">
<head>
<meta charset="utf-8">
<title>Tarnvel Software – Internship Flyer</title>
<link rel="stylesheet" href="https://fonts.googleapis.com/css2?family=Comfortaa:wght@400;700&family=Gloria+Hallelujah&display=swap">
<style>
  :root {
    --water-top: #b9bfbf;
    --water-mid: #8f9796;
    --water-low: #a8aeac;
    --header-bg: #ffffff;
    --brand-grey: #4a4a4a;
    --red: #ec2029;
    --orange: #f47a3a;
    --yellow: #fff200;
    --green: #1aab4b;
    --blue: #10b3ee;
    --ink: #1a1a1a;
    --white: #ffffff;
    --cream: #fff6c8;
    --link: #2a9fd8;
    --plank-light: #e4e3df;
    --plank-mid: #c9c6bf;
    --wood-brown: #8a5a32;
    --wood-dark: #5e3a1e;
    --cta-bg: #111111;
  }
  * { box-sizing: border-box; margin: 0; padding: 0; }
  html, body { width: 927px; height: 1200px; overflow: hidden; background: #fff; }
  .flyer {
    position: relative; width: 927px; height: 1200px; overflow: hidden;
    font-family: "Comfortaa", sans-serif;
  }
  .water-photo {
    position: absolute; left: 0; top: 0; width: 927px; height: 833px;
    background: linear-gradient(180deg, var(--water-top) 0%, var(--water-mid) 40%, var(--water-low) 100%);
  }
  .header-band {
    position: absolute; left: 0; top: 50px; width: 927px; height: 89px;
    background: var(--header-bg);
    display: flex; align-items: center; padding-left: 84px;
  }
  .brand {
    display: flex; align-items: center; gap: 8px;
    font-weight: 700; font-size: 24px; color: var(--brand-grey);
  }
  .brand-dot { width: 14px; height: 14px; border-radius: 50%; background: var(--brand-grey); }

  .stroke {
    position: absolute;
    clip-path: polygon(1% 8%, 6% 0, 40% 4%, 75% 0, 97% 6%, 100% 30%, 98% 62%, 100% 92%, 88% 100%, 50% 96%, 12% 100%, 2% 94%, 0 60%, 2% 30%);
    display: flex; flex-direction: column; justify-content: center; align-items: center;
    text-align: center; line-height: 1.15;
  }
  .stroke-red { left: 401px; top: 164px; width: 516px; height: 51px; background: var(--red); color: var(--cream); font-size: 30px; }
  .stroke-orange { left: 295px; top: 247px; width: 493px; height: 109px; background: var(--orange); color: var(--white); font-size: 31px; }
  .stroke-orange .sub { font-size: 26px; margin-top: 4px; }
  .stroke-yellow { left: 288px; top: 379px; width: 545px; height: 48px; background: var(--yellow); color: var(--red); font-size: 30px; flex-direction: row; align-items: baseline; padding-top: 4px; }
  .stroke-yellow .big { font-size: 42px; margin-right: 8px; }
  .stroke-green { left: 159px; top: 455px; width: 629px; height: 121px; background: var(--green); color: var(--white); font-size: 29px; }
  .stroke-green .tiny { font-size: 13px; color: var(--yellow); vertical-align: 14px; }
  .stroke-blue { left: 212px; top: 606px; width: 682px; height: 197px; background: var(--blue); color: var(--ink); font-size: 29px; }
  .stroke-blue .mark { background: var(--yellow); padding: 0 4px; }
  .stroke-blue .huge { color: var(--yellow); font-size: 50px; font-weight: 700; vertical-align: -6px; }
  .star { font-size: 1.15em; margin-right: 6px; }

  .wood-photo {
    position: absolute; left: 0; top: 833px; width: 927px; height: 367px;
    background: linear-gradient(180deg, var(--plank-light) 0%, var(--plank-mid) 55%, var(--wood-brown) 64%, var(--wood-dark) 100%);
  }
  .crayon { position: absolute; height: 14px; border-radius: 4px; }
  .crayon-green { left: 18px; top: 900px; width: 200px; background: #2f5a2e; transform: rotate(22deg); }
  .crayon-yellow { left: 690px; top: 893px; width: 165px; background: #d8b21c; transform: rotate(-6deg); }
  .pencil { left: 530px; top: 1018px; width: 340px; background: #e0883a; transform: rotate(-14deg); }

  .contact {
    position: absolute; left: 220px; top: 852px; color: var(--ink);
    font-size: 27px; line-height: 1.45;
  }
  .contact .indent { padding-left: 42px; }
  .contact a { color: var(--link); text-decoration: underline; }
  .arrow { position: absolute; left: 282px; top: 990px; }

  .more-info { position: absolute; left: 45px; top: 1078px; color: var(--white); font-size: 27px; }
  .more-1 { position: absolute; left: 200px; top: 1112px; color: var(--white); font-size: 30px; }
  .more-2 { position: absolute; left: 162px; top: 1136px; color: var(--white); font-size: 56px; font-weight: 700; }

  .cta {
    position: absolute; left: 477px; top: 1124px; width: 450px; height: 65px;
    background: var(--cta-bg);
    clip-path: polygon(2% 10%, 30% 0, 70% 6%, 100% 0, 100% 100%, 60% 94%, 20% 100%, 0 90%);
    color: var(--white); font-family: "Gloria Hallelujah", cursive; font-size: 31px;
    display: flex; align-items: center; padding-left: 42px;
  }
</style>
</head>
<body>
<main class="flyer">
  <div class="water-photo" role="img" aria-label="Photo of calm grey lake water"></div>

  <header class="header-band">
    <div class="brand"><span>Tarnvel</span><span class="brand-dot"></span><span>Software</span></div>
  </header>

  <div class="stroke stroke-red"><p><span class="star">*</span> 8th grade to 12th grade</p></div>
  <div class="stroke stroke-orange">
    <p><span class="star">*</span>Land a real job internship</p>
    <p class="sub">(instead of Krovetts)</p>
  </div>
  <div class="stroke stroke-yellow"><span class="big">*100's</span><span>of internships available</span></div>
  <div class="stroke stroke-green">
    <p><span class="star">*</span>Learn how to start your own business</p>
    <p>out of High School</p>
    <p>making way more than <span class="tiny">minimum</span> wage</p>
  </div>
  <div class="stroke stroke-blue">
    <p><span class="star">*</span>In college when interviewing</p>
    <p>for an internship,</p>
    <p><span class="mark">don't be the</span> guy that answers</p>
    <p>"no, sorry, this would be my first internship"</p>
    <p>putting you at a <span class="huge">huge</span> disadvantage</p>
  </div>

  <div class="wood-photo" role="img" aria-label="Photo of weathered wooden planks, light grey above and brown below"></div>
  <div class="crayon crayon-green" role="img" aria-label="Green crayon lying on the planks"></div>
  <div class="crayon crayon-yellow" role="img" aria-label="Yellow crayon lying on the planks"></div>
  <div class="crayon pencil" role="img" aria-label="Orange pencil lying on the planks"></div>

  <div class="contact">
    <p><span class="star">*</span>Fill in the Contact Us form at</p>
    <p class="indent"><a href="http://tarnvelsw.com">http://tarnvelsw.com</a> at the</p>
    <p>bottom left corner</p>
  </div>

  <svg class="arrow" width="60" height="84" viewBox="0 0 60 84" aria-hidden="true">
    <path d="M40 4 C22 6 18 26 34 26 C48 26 44 8 30 12 C18 34 14 54 10 74" fill="none" stroke="#111" stroke-width="3" stroke-linecap="round"/>
    <path d="M2 62 L10 78 L24 66" fill="none" stroke="#111" stroke-width="3" stroke-linecap="round" stroke-linejoin="round"/>
  </svg>

  <p class="more-info">to find out more information</p>
  <p class="more-1">more</p>
  <p class="more-2">more</p>

  <div class="cta">claim your spot today !</div>
</main>
</body>
</html>
```